Etiketten-Design für Honiggläser
Zielgruppe
kleine Hobby-Imkerei, Zielgruppe 'Regionale Käufer', die gerne Wissen, wo ihr Honig her kommt. Mittleres Preissegment
Aufgabenstellung
Das Etikett soll für meine Honiggläser dienen. Die Maße sind 134 x 64 mm. Die Breite kann bis 150 mm variieren, die Höhe nicht.
Pflichtangaben : 'Deutscher xxx Honig (z.B. Blütenhonig), Name und Anschrift (Jonas Welke Birkenweg 12 73512 Ludwigsburg J.Welke@postfeld.de), mindestens haltbar bis(wird gestempelt, Fläche min. 30x7mm, Gewicht 500 g(Schriftgröße min. 4 mm), 'Mehrwegglas'. Schriftgröße mindestens 1,2mm bezogen auf das kleine „x“. Optional Lagerbedingungen, s. bisheriges Etikett.
Das angehängte Bild soll in irgendeiner Form mit eingebunden wäre, gerne können Farben und Form aber verändert werden, Bildrechte sind bei mir. Anbei auch mein bisheriges, selber entworfenes Etikett.
Das neue Etikett soll moderner und ansprechender werden, der Regionalitätsbezug etwas besser herausgearbeitet werden. Gelb hat sich als Farbe nicht bewährt, da das gelb des Honig sich manchmal beißt.

```html
<!DOCTYPE html>
<html lang="de">
<head>
<meta charset="utf-8">
<title>Honigetikett – Imkerei Jonas Welke</title>
<link href="https://fonts.googleapis.com/css2?family=Amatic+SC:wght@400;700&display=swap" rel="stylesheet">
<style>
  :root {
    --page: #ffffff;
    --label-bg: #eeeade;
    --panel: #f3f0e7;
    --ribbon: #ffffff;
    --ribbon-edge: #e2ddd0;
    --ink: #262422;
    --meadow: #4f8a3a;
    --meadow-dark: #2f5e25;
    --sky: #d9ddd6;
    --blossom: #f4f2ea;
    --flag-black: #1a1a1a;
    --flag-red: #d0161b;
    --flag-gold: #f2b70f;
  }
  * { margin: 0; padding: 0; box-sizing: border-box; }
  html, body {
    width: 848px; height: 1200px; overflow: hidden;
    background: var(--page);
  }
  body { position: relative; font-family: "Amatic SC", "Comic Sans MS", cursive; color: var(--ink); }

  .label {
    position: absolute; left: 131px; top: 776px;
    width: 625px; height: 298px;
    background: var(--label-bg);
  }
  .label__panel {
    position: absolute; left: 222px; top: 0; width: 163px; height: 100%;
    background: var(--panel);
  }
  .label__ribbon {
    position: absolute; left: 236px; top: 0; width: 135px; height: 276px;
  }
  .label__heart {
    position: absolute; left: 243px; top: 30px; width: 121px; height: 110px;
  }
  .label__bee {
    position: absolute; left: 296px; top: 150px; width: 16px; height: 10px;
    border-radius: 50%;
    background: radial-gradient(circle at 50% 50%, #a9a49a, #cfcac0);
  }
  .label__title {
    position: absolute; left: 236px; width: 135px; top: 164px;
    text-align: center; font-weight: 700; font-size: 19px; line-height: 18px;
  }
  .label__keeper {
    position: absolute; left: 236px; width: 135px; top: 202px;
    text-align: center; font-weight: 700; font-size: 14px;
  }
  .label__flag {
    position: absolute; left: 295px; top: 226px; width: 18px; height: 12px;
  }

  .label__storage {
    position: absolute; left: 40px; width: 160px; top: 118px;
    text-align: center; font-weight: 700; font-size: 12.5px; line-height: 13px;
  }
  .label__info {
    position: absolute; left: 433px; width: 160px; top: 100px;
    text-align: center; font-weight: 700;
  }
  .label__address { font-size: 12.5px; line-height: 13px; }
  .label__weight { font-size: 24px; line-height: 24px; margin-top: 14px; }
  .label__type { font-size: 12.5px; line-height: 13px; margin-top: 2px; }
  .label__recycle { display: block; margin: 6px auto 0; width: 16px; height: 16px; }
</style>
</head>
<body>
  <section class="label">
    <div class="label__panel"></div>

    <svg class="label__ribbon" viewBox="0 0 135 276" aria-hidden="true">
      <path d="M0 0 H135 V276 L67.5 256 L0 276 Z" fill="var(--ribbon)" stroke="var(--ribbon-edge)" stroke-width="1.5"/>
    </svg>

    <svg class="label__heart" viewBox="0 0 100 90" role="img" aria-label="Gemalte Landschaft mit blühenden Bäumen, grüner Wiese und drei weißen Bienenstöcken">
      <defs>
        <linearGradient id="scene" x1="0" y1="0" x2="0" y2="1">
          <stop offset="0" stop-color="var(--blossom)"/>
          <stop offset="0.3" stop-color="var(--sky)"/>
          <stop offset="0.45" stop-color="var(--meadow)"/>
          <stop offset="1" stop-color="var(--meadow-dark)"/>
        </linearGradient>
      </defs>
      <path d="M50 88 C20 66 2 46 2 26 C2 11 14 2 27 2 C38 2 46 9 50 17 C54 9 62 2 73 2 C86 2 98 11 98 26 C98 46 80 66 50 88 Z"
            fill="url(#scene)" stroke="#ffffff" stroke-width="4"/>
    </svg>

    <div class="label__bee" role="img" aria-label="Kleine Biene"></div>

    <h1 class="label__title">Deutscher Honig<br>aus Ludwigsburg</h1>
    <p class="label__keeper">Imkerei Jonas Welke</p>

    <svg class="label__flag" viewBox="0 0 18 12" aria-label="Deutschlandflagge" role="img">
      <rect x="0" y="0" width="18" height="4" fill="var(--flag-black)"/>
      <rect x="0" y="4" width="18" height="4" fill="var(--flag-red)"/>
      <rect x="0" y="8" width="18" height="4" fill="var(--flag-gold)"/>
    </svg>

    <p class="label__storage">
      Trocken, kühl und<br>
      dunkel lagern.<br>
      Kristallisierter Honig<br>
      kann im Wasserbad bis<br>
      max. 40 °C wieder<br>
      verflüssigt werden.
    </p>

    <div class="label__info">
      <p class="label__address">
        Imkerei Jonas Welke<br>
        Birkenweg 12<br>
        73512 Ludwigsburg<br>
        j.welke@postfeld.de
      </p>
      <p class="label__weight">500 g</p>
      <p class="label__type">Deutscher Imkerhonig<br>im Mehrwegglas</p>
      <svg class="label__recycle" viewBox="0 0 16 16" role="img" aria-label="Mehrweg-Symbol">
        <g fill="none" stroke="var(--ink)" stroke-width="1.6" stroke-linecap="round">
          <path d="M3 9 A5 5 0 0 1 11 4"/>
          <path d="M13 7 A5 5 0 0 1 5 12"/>
        </g>
        <path d="M9.5 2 L12.5 4.3 L9.3 5.8 Z" fill="var(--ink)"/>
        <path d="M6.5 14 L3.5 11.7 L6.7 10.2 Z" fill="var(--ink)"/>
      </svg>
    </div>
  </section>
</body>
</html>
```